New River III Precinct 6x11 GOTV postcard

We require BOTH persuasive copy and high-impact layout for an oversized 6x11 political mailer. This might be one person, but it likely requires a specialized "creative team." of an experienced political strategist copywriter PLUS a graphic designer - so the words fit the exact layout block, and the visuals reinforce the psychological punch of the headline.

The goal is to remove all excuses a targeted audience of ~900 registered Harvestline + ~1800 Unaffiliated voters in our precinct - have for not voting.

I need to be able to work by phone / online chat to iterate designs
I need to own the design in the top couple of software outputs that any printer service will require.

I want to experiment with very subtle background images as follows:
- Front of postcard that conveys "CHANGE" of not just seasons - but of encouraging change of precinct voter representation - so anything about fall foliage / conveyance of change tie-in is worthy of considering
- Back of postcard - any Appalachian long rage mountain view that includes 5-7 layers of hills in the distance.
Some photos as samples to consider.

Target Market(s)

~2,700 registered Harvestliners and Unaffiliated voters

Requirements
Must have
• We require BOTH persuasive copy and high-impact layout for an oversized 6x11 political mailer. This might be one person, but it likely requires a specialized "creative team." of an experienced political strategist copywriter PLUS a graphic designer - so the words fit the exact layout block, and the visuals reinforce the psychological punch of the headline
Nice to have
• subtle background photos

```html
<!DOCTYPE html>
<html lang="en">
<head>
<meta charset="utf-8">
<title>Vote for New Representation – Postcard Back</title>
<link rel="stylesheet" href="https://fonts.googleapis.com/css2?family=Oswald:wght@600;700&family=Roboto:wght@400;700&family=Roboto+Condensed:wght@400;700&display=swap">
<style>
  :root {
    --navy: #0e1a5c;
    --crimson: #8c0a2f;
    --gold: #e3a829;
    --ink: #1b1b24;
    --white: #ffffff;
  }
  * { margin: 0; padding: 0; box-sizing: border-box; }
  html, body { width: 1200px; height: 666px; overflow: hidden; background: #fff; }
  .postcard {
    position: relative;
    width: 1200px; height: 666px; overflow: hidden;
    font-family: "Roboto", Arial, sans-serif;
    color: var(--ink);
  }
  .backdrop {
    position: absolute; inset: 0;
    background: linear-gradient(180deg, #fbe6da 0%, #f7ead9 14%, #eef0f2 30%, #d9e3f2 48%, #c6d6ee 65%, #b9cdea 82%, #b4c6a4 94%, #6f8a52 100%);
  }
  .headline { position: absolute; left: 0; top: 0; width: 1200px; height: 137px; }
  .headline svg { display: block; width: 1200px; height: 137px; }
  .headline text {
    font-family: "Oswald", "Arial Narrow", sans-serif; font-weight: 700; font-size: 102px;
  }
  .headline .lead { fill: var(--navy); }
  .headline .accent { fill: var(--crimson); }
  .pain-band {
    position: absolute; left: 50px; top: 137px; width: 1101px; height: 60px;
    background: var(--navy); padding: 6px 0 0 72px;
    color: var(--white);
  }
  .pain-band h2 { font-weight: 700; font-size: 22.5px; color: var(--gold); line-height: 1.15; }
  .pain-band p { font-weight: 700; font-size: 16.8px; line-height: 1.35; margin-top: 1px; }
  .issue { position: absolute; width: 310px; }
  .issue .icon { position: absolute; left: -58px; top: 4px; width: 42px; height: 42px; }
  .issue h3 {
    font-family: "Roboto Condensed", "Arial Narrow", sans-serif; font-weight: 700;
    font-size: 17px; color: var(--crimson); line-height: 1.05;
  }
  .issue p { font-size: 13.4px; line-height: 16.2px; margin-top: 1px; }
  .ballot {
    position: absolute; left: 838px; top: 212px; width: 313px; height: 363px;
    border: 2px solid var(--navy); border-radius: 9px; overflow: hidden;
    background: rgba(255,255,255,.35);
    font-family: "Roboto Condensed", "Arial Narrow", sans-serif; font-weight: 700;
  }
  .ballot-head {
    background: var(--navy); color: var(--gold); height: 62px;
    padding: 4px 0 0 19px; font-size: 23.5px; line-height: 1.0;
  }
  .ballot-list { list-style: none; padding: 11px 0 0 12px; }
  .ballot-list li { display: flex; font-size: 13.4px; line-height: 1.22; align-items: flex-end; margin-bottom: 7px; }
  .ballot-list .office { width: 162px; color: var(--navy); }
  .ballot-list .pick { color: var(--crimson); }
  .ballot-list .pick::before { content: "- "; color: var(--navy); }
  .footer-band {
    position: absolute; left: 46px; top: 599px; width: 1108px; height: 28px;
    background: var(--navy); color: var(--white);
    font-family: "Roboto Condensed", "Arial Narrow", sans-serif; font-size: 20px;
    text-align: center; line-height: 28px; letter-spacing: .2px;
  }
  .footer-band .star { color: var(--gold); margin: 0 8px; }
</style>
</head>
<body>
<main class="postcard">
  <div class="backdrop" role="img" aria-label="Soft background photo of layered Appalachian mountain ridges fading into a pale sunset sky, with treetops along the bottom edge"></div>

  <h1 class="headline">
    <svg viewBox="0 0 1200 137" aria-label="Vote for new representation">
      <text x="80" y="123" textLength="1037" lengthAdjust="spacingAndGlyphs"><tspan class="lead">VOTE FOR </tspan><tspan class="accent">NEW REPRESENTATION</tspan></text>
    </svg>
  </h1>

  <section class="pain-band">
    <h2>LOCAL PAIN – THANKS TO CURRENT REPRESENTATIVES –</h2>
    <p>and sadly, to avoid accountability, they’ve cleverly delayed many / most impacts until AFTER the 2026 election.</p>
  </section>

  <article class="issue" style="left:122px; top:211px;">
    <svg class="icon" viewBox="0 0 42 42" aria-hidden="true" fill="var(--navy)">
      <circle cx="8" cy="9" r="4"/><rect x="3" y="14" width="10" height="14" rx="3"/>
      <circle cx="20" cy="12" r="3"/><rect x="16" y="16" width="8" height="11" rx="2"/>
      <circle cx="31" cy="7" r="3.5"/><rect x="2" y="29" width="22" height="5" rx="2"/>
      <circle cx="30" cy="30" r="9"/>
      <text x="30" y="35" font-size="13" font-family="Roboto" font-weight="700" fill="#fff" text-anchor="middle">$</text>
    </svg>
    <h3>FAMILY BUDGET –</h3>
    <p>exploded costs for everything: groceries, gas,<br>car insurance, rent.</p>
  </article>

  <article class="issue" style="left:122px; top:279px; width:310px;">
    <svg class="icon" viewBox="0 0 42 42" aria-hidden="true" style="top:10px">
      <path d="M21 38 L5 22 A9 9 0 0 1 21 9 A9 9 0 0 1 37 22 Z" fill="var(--navy)"/>
      <rect x="19" y="14" width="4" height="16" fill="#fff"/><rect x="13" y="20" width="16" height="4" fill="#fff"/>
    </svg>
    <h3>HEALTH –</h3>
    <p>expired subsidies, tax credits mean families in NC will lose coverage or pay more. 50% cuts to hospitals, mental health facilities; rural facilities will be closing.</p>
  </article>

  <article class="issue" style="left:122px; top:378px;">
    <svg class="icon" viewBox="0 0 42 42" aria-hidden="true">
      <circle cx="21" cy="11" r="8" fill="var(--navy)"/>
      <circle cx="21" cy="10" r="3" fill="none" stroke="#fff" stroke-width="1.8"/>
      <path d="M21 13 V18 M18.5 16 H23.5" stroke="#fff" stroke-width="1.8"/>
      <path d="M3 22 L9 36 H18 V30 L12 24 Z M39 22 L33 36 H24 V30 L30 24 Z" fill="var(--navy)"/>
    </svg>
    <h3>REPRODUCTIVE RIGHTS –</h3>
    <p>Government authoritarian intrusion –<br>censure women’s rights.</p>
  </article>

  <article class="issue" style="left:122px; top:446px; width:320px;">
    <svg class="icon" viewBox="0 0 42 42" aria-hidden="true">
      <path d="M19 2 L34 7 V21 C34 30 27 36 19 40 C11 36 4 30 4 21 V7 Z" fill="var(--navy)"/>
      <path d="M14 11 V19 C14 21 16 22 17 22 V32 M20 11 V19 C20 21 18 22 17 22 M17 11 V18 M24 11 C27 13 27 20 24 21 V32" stroke="#fff" stroke-width="2" fill="none"/>
      <circle cx="33" cy="34" r="6" fill="var(--navy)" stroke="#fff" stroke-width="1.5"/>
      <path d="M30 34 L32.5 36.5 L36 32" stroke="#fff" stroke-width="1.6" fill="none"/>
    </svg>
    <h3>FOOD SECURITY –</h3>
    <p>Weaponized hunger – cuts to SNAP;<br>school meals cut; additional work requirements.</p>
  </article>

  <article class="issue" style="left:122px; top:514px; width:310px;">
    <svg class="icon" viewBox="0 0 42 42" aria-hidden="true">
      <path d="M3 8 C10 5 16 6 20 9 V36 C16 33 10 33 3 35 Z M39 8 C32 5 26 6 22 9 V36 C26 33 32 33 39 35 Z" fill="none" stroke="var(--navy)" stroke-width="3.5" stroke-linejoin="round"/>
      <path d="M1 37 H41" stroke="var(--navy)" stroke-width="3"/>
    </svg>
    <h3>EDUCATION –</h3>
    <p>Watauga $2.2mm shortfall personnel cuts, freezes in hiring, teacher training.Abandoning civil rights of Special Ed students to HHS and DOL.</p>
  </article>

  <article class="issue" style="left:513px; top:208px; width:304px;">
    <svg class="icon" viewBox="0 0 42 42" aria-hidden="true" style="left:-58px; top:8px">
      <path d="M21 3 L40 19 L37 22 L21 9 L5 22 L2 19 Z" fill="var(--navy)"/>
      <rect x="6" y="5" width="5" height="9" fill="var(--navy)"/>
      <path d="M8 20 L21 10 L34 20 V38 H8 Z" fill="var(--navy)"/>
      <rect x="12" y="24" width="5" height="7" fill="#fff"/><rect x="25" y="24" width="5" height="7" fill="#fff"/>
      <rect x="18.5" y="24" width="5" height="14" fill="#fff"/>
    </svg>
    <h3>HOUSING –</h3>
    <p>~25% of renters are spending over 50% of income on rent. Especially bad locally; predatory leasing terms and skyrocketing rents. Proposed legislation is transforming HUD with the goal of getting rid of Section 8 housing that cares for vulnerable populations.</p>
  </article>

  <article class="issue" style="left:513px; top:340px; width:300px;">
    <svg class="icon" viewBox="0 0 42 42" aria-hidden="true" style="left:-58px; top:2px">
      <path d="M8 10 A17 17 0 0 1 34 9 M38 17 A17 17 0 0 1 30 36 M21 39 A17 17 0 0 1 4 22" fill="none" stroke="var(--navy)" stroke-width="3.5"/>
      <path d="M34 4 V11 H27 M34 40 L30 36 L36 33 M2 26 L4 20 L9 24" fill="none" stroke="var(--navy)" stroke-width="3"/>
      <path d="M24 8 L13 24 H20 L17 35 L29 18 H22 Z" fill="var(--navy)"/>
    </svg>
    <h3>ENERGY –</h3>
    <p>In 2022 Boone achieved 100% renewable energy in town buildings; this is now being destroyed by repeal of renewable energy project funding.<br>Ridge State Innovation District prepares renewable workforce technologies – all this is now in limbo.</p>
  </article>

  <article class="issue" style="left:513px; top:456px; width:290px;">
    <svg class="icon" viewBox="0 0 42 42" aria-hidden="true" style="left:-58px; top:0">
      <circle cx="19" cy="21" r="17" fill="none" stroke="var(--navy)" stroke-width="2.5"/>
      <ellipse cx="19" cy="21" rx="7" ry="17" fill="none" stroke="var(--navy)" stroke-width="2.2"/>
      <path d="M2 21 H36 M5 12 H33 M5 30 H26" stroke="var(--navy)" stroke-width="2.2"/>
      <path d="M40 14 C28 14 20 22 22 38 C34 38 41 30 40 14 Z" fill="var(--navy)"/>
    </svg>
    <h3>ENVIRONMENT –</h3>
    <p>Reduced protections from coal ash pond leaks threaten public health. Corporations not held responsible for damage; public picks up the tab. Environmental Justice enforcement no longer a priority. Logging in Watauga with no public oversight. It’s the “haz-mat” model: do nothing, wait for catastrophe, then fix it.</p>
  </article>

  <aside class="ballot">
    <h2 class="ballot-head">SAMPLE BALLOT<br>RECOMMENDATIONS</h2>
    <ul class="ballot-list">
      <li><span class="office">US SENATE</span><span class="pick">RAY CALLISTER</span></li>
      <li><span class="office">US HOUSE – DISTRICT 5</span><span class="pick">CHET HALVORSEN</span></li>
      <li><span class="office">REQMT TO SHOW ID FOR VOTERS NOT IN PERSON</span><span class="pick">NO</span></li>
      <li><span class="office">STATE SENATE DISTRICT 47</span><span class="pick">FRED HOLLINS</span></li>
      <li><span class="office">HOUSE OF REP’S<br>DISTRICT 93</span><span class="pick">CARL WHITAKER</span></li>
      <li><span class="office">NC SUPREME COURT</span><span class="pick">ALMA EVERS</span></li>
      <li><span class="office">NC COURT OF APPEALS –<br>SEAT 1</span><span class="pick">JOEL ASHCOMBE</span></li>
      <li><span class="office">NC COURT OF APPEALS –<br>SEAT 2</span><span class="pick">TOBIN HARWELL</span></li>
      <li><span class="office">NC COURT OF APPEALS –<br>SEAT 3</span><span class="pick">CORINNE WEXLER</span></li>
    </ul>
  </aside>

  <footer class="footer-band">
    YOUR COMMUNITY<span class="star">★</span>YOUR VOICE<span class="star">★</span>YOUR VOTE<span class="star">★</span>THIS NOVEMBER, VOTE FOR NEW
  </footer>
</main>
</body>
</html>
```